Brochure required for international Sports event

We need an 8 page brochure designed for an international sports event to be hosted in Japan. We are a Travel Company providing packages for participants looking to travel to the event.
The brochure will feature information on the event as well as services our company can provide.
The Brochure is to be an 8 page A4 document in portrait layout.
The brochure needs to be provided both as a print ready document and digital brochure for emailing.
Brochure structure, copy, logo and imagery has been provided
As well as a example brochure design that we like for inspiration.
Link to icons - https://www.filevault-example.net/sh/kq3mzplr8wbtyoc/BBBxkTLmQ4pR7Hs2nW6vYbCgE?dl=0
Target Market(s)
Masters/Veterans Sports Participants
Industry/Entity Type
Travel
Colors
Designer to choose colors to be used in the design.
Look and feel
Each slider illustrates characteristics of the customer's brand and the style your logo design should communicate.

```html
<!DOCTYPE html>
<html lang="en">
<head>
<meta charset="utf-8">
<title>Global Veterans Games 2021 – Hoshino Trails Brochure</title>
<link rel="stylesheet" href="https://fonts.googleapis.com/css2?family=Exo+2:ital,wght@0,600;0,700;0,800;1,700;1,800&family=Montserrat:ital,wght@0,400;0,500;0,600;1,400;1,500&display=swap">
<style>
:root{
  --stage:#d6d6d6;
  --paper:#ffffff;
  --paper-cool:#eceef2;
  --red:#d4202a;
  --red-deep:#7e1f17;
  --red-mid:#a83225;
  --ink:#1d1d1f;
  --ink-soft:#4c4d53;
  --slate:#9aa3b4;
  --band:rgba(212,32,42,.2);
  --band-strong:rgba(212,32,42,.55);
  --grey-band:rgba(120,125,135,.14);
}
*{box-sizing:border-box;margin:0;padding:0}
html,body{width:1200px;height:2490px;overflow:hidden;background:var(--stage)}
body{font-family:"Montserrat",sans-serif;color:var(--ink)}
ul{list-style:none}
.stage{position:relative;width:1200px;height:2490px}
.spread{position:absolute;left:100px;width:1000px;height:707px;display:flex;box-shadow:0 12px 30px rgba(0,0,0,.18)}
.spread--cover{top:61px}
.spread--intro{top:891px}
.spread--travel{top:1721px}
.page{position:relative;width:500px;height:707px;overflow:hidden;background:var(--paper)}
.page + .page{border-left:1px solid rgba(0,0,0,.08)}
.photo{position:absolute;display:block}
.heading{position:absolute;font-family:"Exo 2",sans-serif;font-style:italic;font-weight:800;color:var(--red);text-transform:uppercase;letter-spacing:.5px;line-height:1}
.body-copy{font-size:8.6px;line-height:1.6;color:var(--ink-soft);font-style:italic}
.body-copy p + p{margin-top:5px}
.slash{position:absolute;background:var(--band);transform:skewX(-28deg)}
.slash--strong{background:var(--band-strong)}
.slash--grey{background:var(--grey-band)}
.slash--line{background:rgba(90,95,105,.55)}

/* back cover */
.back-cover{background:linear-gradient(160deg,#dfe5ee,#f4f5f8 60%)}
.back-cover__photo{left:0;top:150px;width:500px;height:557px;background:linear-gradient(180deg,#d8e0ea 0%,#c9d2df 12%,#c8402e 30%,#b33527 48%,#8e8f93 66%,#b9bbbf 82%,#d9dadd 100%)}
.back-cover__year{position:absolute;left:60px;top:52px;font-family:"Exo 2",sans-serif;font-style:italic;font-weight:800;font-size:92px;color:var(--slate);opacity:.75;line-height:1;z-index:2}
.back-cover__event{position:absolute;left:290px;top:56px;font-family:"Exo 2",sans-serif;font-weight:700;font-size:17px;line-height:1.05;color:var(--slate);text-transform:uppercase;z-index:2}
.back-cover__rule{position:absolute;left:290px;height:2px;width:95px;background:var(--slate);z-index:2}
.back-cover__place{position:absolute;left:66px;top:144px;font-family:"Exo 2",sans-serif;font-weight:700;font-size:17px;color:var(--slate);letter-spacing:1px;z-index:2}
.back-cover__contact{position:absolute;left:0;right:0;bottom:0;padding:18px 36px 26px;text-align:right;font-style:normal;font-size:13px;font-weight:500;line-height:1.4;color:var(--ink);background:linear-gradient(180deg,rgba(230,232,236,0),rgba(230,232,236,.95) 35%)}

/* front cover */
.front-cover__photo{left:0;top:0;width:500px;height:707px;background:linear-gradient(135deg,#6f1a13,var(--red-mid) 40%,#94281e 65%,#4e120d)}
.front-cover__year{position:absolute;left:64px;top:62px;font-family:"Exo 2",sans-serif;font-style:italic;font-weight:800;font-size:108px;color:#fff;line-height:1}
.front-cover__event{position:absolute;left:76px;top:180px;font-family:"Exo 2",sans-serif;font-weight:800;font-size:19px;line-height:1.1;color:#fff;text-transform:uppercase}
.front-cover__rule{position:absolute;left:205px;top:213px;width:110px;height:3px;background:#fff}
.front-cover__date{position:absolute;left:58px;top:236px;width:345px;padding:6px 0 6px 24px;background:#fff;font-family:"Exo 2",sans-serif;font-style:italic;font-weight:800;font-size:17px;color:var(--red)}
.brand{position:absolute;right:70px;bottom:104px;font-family:"Exo 2",sans-serif;font-weight:800;color:#fff;font-size:34px;line-height:1;text-align:right;text-transform:uppercase}
.brand small{display:block;font-size:21px;margin-top:4px}

/* intro spread */
.intro__title{left:48px;top:34px;font-size:20px}
.intro__lead{position:absolute;left:48px;top:64px;width:404px}
.intro__kansai{left:48px;top:158px;font-size:18px}
.intro__kansai-copy{position:absolute;left:48px;top:184px;width:404px}
.intro__photo{left:0;top:325px;width:500px;height:382px;background:linear-gradient(160deg,#f1f3ef 0%,#9cc26a 20%,#e0d86a 45%,#c9b9a4 68%,#4f6a52 100%)}

.sports{background:linear-gradient(180deg,#fff,var(--paper-cool))}
.sports__title{left:30px;top:24px;font-size:18px}
.sports__lead{position:absolute;left:30px;top:46px;width:190px}
.sports__photo{left:310px;top:24px;width:190px;height:110px;background:linear-gradient(120deg,#c5c8cd,#c2763c 55%,#8a5228)}
.sports__rows{position:absolute;left:0;top:150px;width:500px;height:540px;background:repeating-linear-gradient(180deg,transparent 0 22px,var(--grey-band) 22px 36px)}
.sports__grid{position:absolute;left:22px;top:146px;width:460px;display:grid;grid-template-columns:repeat(4,1fr);grid-auto-flow:column;grid-template-rows:repeat(9,59px)}
.sport{display:flex;flex-direction:column;align-items:center;gap:4px}
.sport svg{width:24px;height:24px;fill:var(--ink)}
.sport__name{font-size:8.6px;font-style:italic;color:var(--ink-soft);white-space:nowrap}

/* travel spread */
.venues__title{left:34px;top:62px;font-size:20px}
.venues__map{left:34px;top:92px;width:436px;height:580px;background:linear-gradient(135deg,#3aa8e0 0%,#6f52b5 25%,#2f9a5c 45%,#b7a33a 58%,#f0a531 72%,#ee6fa8 100%)}
.tour__title{left:36px;top:36px;font-size:20px}
.tour__lead{position:absolute;left:36px;top:62px;width:420px}
.tour__sub{position:absolute;left:36px;top:128px;font-size:14px;color:var(--ink-soft)}
.tour__list{position:absolute;top:156px;font-family:"Exo 2",sans-serif;font-weight:700;font-size:11.5px;text-transform:uppercase;color:var(--ink)}
.tour__list--main{left:36px}
.tour__list--extra{left:270px;text-transform:none;font-size:12px}
.tour__list li{display:flex;align-items:flex-start;gap:9px;margin-bottom:8px;line-height:1.15}
.tour__list svg{flex:none;fill:var(--ink)}
.tour__photo{left:0;top:400px;width:500px;height:307px;background:linear-gradient(90deg,#2c3a6a,#4a5a8a 15%,#c23a3a 40%,#a8304c 60%,#7a2b4a 78%,#6b6f76)}
</style>
</head>
<body>
<svg width="0" height="0" style="position:absolute" aria-hidden="true">
  <symbol id="i-cup" viewBox="0 0 24 24"><path d="M6 3h12v3h3v2a4 4 0 0 1-4 4h-.4A5 5 0 0 1 13 15v3h3v3H8v-3h3v-3a5 5 0 0 1-3.6-3H7a4 4 0 0 1-4-4V6h3zM5 8a2 2 0 0 0 1.2 1.9L6 8zm14 0h-1l-.2 1.9A2 2 0 0 0 19 8z"/></symbol>
  <symbol id="i-ball" viewBox="0 0 24 24"><path d="M12 2a10 10 0 1 0 0 20 10 10 0 0 0 0-20zm0 2a8 8 0 0 1 6.3 3.1C15.5 8 13 10.2 12 13 11 10.2 8.5 8 5.7 7.1A8 8 0 0 1 12 4zM4.6 9c2.5.7 4.8 2.9 5.6 6.3L10 20A8 8 0 0 1 4.6 9zM14 20l-.2-4.7C14.6 11.9 17 9.7 19.4 9A8 8 0 0 1 14 20z"/></symbol>
  <symbol id="i-oval" viewBox="0 0 24 24"><path d="M12 5c6 0 10 3 10 7s-4 7-10 7S2 16 2 12s4-7 10-7zm-4 6v2h8v-2z"/></symbol>
  <symbol id="i-flag" viewBox="0 0 24 24"><path d="M6 2h2v20H6zM9 3l11 5-11 5z"/></symbol>
  <symbol id="i-medal" viewBox="0 0 24 24"><path d="M7 2h4l1 5 1-5h4l-3 8a6 6 0 1 1-4 0zm5 10a4 4 0 1 0 0 8 4 4 0 0 0 0-8z"/></symbol>
  <symbol id="i-target" viewBox="0 0 24 24"><path d="M12 2a10 10 0 1 0 0 20 10 10 0 0 0 0-20zm0 3a7 7 0 1 1 0 14 7 7 0 0 1 0-14zm0 3a4 4 0 1 0 0 8 4 4 0 0 0 0-8zm0 2.5a1.5 1.5 0 1 1 0 3 1.5 1.5 0 0 1 0-3z"/></symbol>
  <symbol id="i-wave" viewBox="0 0 24 24"><path d="M2 14c3 0 3-3 6-3s3 3 6 3 3-3 6-3h2v3c-2 0-3 3-6 3s-3-3-6-3-3 3-6 3H2zM2 9c3 0 3-3 6-3s3 3 6 3 3-3 6-3h2v3c-2 0-3 3-6 3s-3-3-6-3-3 3-6 3H2z"/></symbol>
  <symbol id="i-sail" viewBox="0 0 24 24"><path d="M12 2v15H4zM13 5l7 12h-7zM3 19h18l-2 3H5z"/></symbol>
  <symbol id="i-bar" viewBox="0 0 24 24"><path d="M1 9h3v6H1zM4 7h3v10H4zM7 11h10v2H7zM17 7h3v10h-3zM20 9h3v6h-3z"/></symbol>
  <symbol id="i-tri" viewBox="0 0 24 24"><path d="M12 2l10 18H2zm0 5L6.5 17h11z"/></symbol>
</svg>
<main class="stage">

  <section class="spread spread--cover" aria-label="Back and front cover">
    <article class="page back-cover">
      <div class="photo back-cover__photo" role="img" aria-label="Photo of a red shrine gate building above stone steps"></div>
      <div class="slash slash--grey" style="left:40px;top:20px;width:26px;height:150px"></div>
      <div class="back-cover__year">2021</div>
      <div class="back-cover__event">Global<br>Veterans<br>Games</div>
      <div class="back-cover__rule" style="top:122px"></div>
      <div class="back-cover__rule" style="top:127px;width:80px"></div>
      <div class="back-cover__place">KANSAI, JAPAN</div>
      <address class="back-cover__contact">www.veterans-trip.example<br>hello@veterans-trip.example<br>PH: +61 2 5550 0142</address>
    </article>
    <article class="page front-cover">
      <div class="photo front-cover__photo" role="img" aria-label="Photo of a corridor of red torii gates"></div>
      <div class="slash" style="left:300px;top:430px;width:60px;height:180px;background:rgba(255,255,255,.08)"></div>
      <div class="slash" style="left:380px;top:470px;width:40px;height:140px;background:rgba(255,255,255,.06)"></div>
      <div class="front-cover__year">2021</div>
      <div class="front-cover__event">Global Veterans Games<br>Kansai, Japan</div>
      <div class="front-cover__rule"></div>
      <div class="front-cover__date">14th to 30th MAY 2021</div>
      <div class="brand">Hoshino<small>Trails</small></div>
    </article>
  </section>

  <section class="spread spread--intro" aria-label="Event and sports pages">
    <article class="page">
      <h2 class="heading intro__title">The Global Veterans Games</h2>
      <div class="body-copy intro__lead">
        <p>The 2021 Global Veterans Games will be the 10th edition of the Games and the first time it will be held in Asia. Since its inception in Toronto in 1985 the Games have grown to become the world's largest mass-participation international sports event.</p>
        <p>The 2021 Games will be held in the Kansai region in the west of Japan and will take place over 17 days from May 14 – 30. An estimated 50,000 participants will meet to play a total of 65 sports and explore this beautiful and alluring country.</p>
      </div>
      <h2 class="heading intro__kansai">Kansai</h2>
      <div class="body-copy intro__kansai-copy">
        <p>Kansai consists of seven prefectures and was formerly the political and cultural centre of Japan for many centuries and includes the cities of Kyoto, Osaka, Nara and Kobe.</p>
        <p>The Kansai region is located in the centre of the Japanese islands and is home to over 20 million people. The region is also host to a number of incredible sights including Osaka Castle, Fushimi Inari Shrine, Kinkaku-ji (the Golden Pavilion), Nara Deer Park, Dotonbori District, Nishiki Markets and Arashiyama Bamboo Grove.</p>
      </div>
      <div class="photo intro__photo" role="img" aria-label="Photo of a veteran runner stretching his leg on a rail"></div>
      <div class="slash" style="left:80px;top:300px;width:60px;height:40px"></div>
      <div class="slash slash--strong" style="left:330px;top:430px;width:90px;height:120px"></div>
      <div class="slash" style="left:410px;top:380px;width:70px;height:90px;background:rgba(212,32,42,.35)"></div>
      <div class="slash slash--line" style="left:395px;top:340px;width:8px;height:28px"></div>
      <div class="slash slash--line" style="left:410px;top:340px;width:14px;height:28px"></div>
    </article>
    <article class="page sports">
      <div class="sports__rows" aria-hidden="true"></div>
      <div class="slash" style="left:320px;top:380px;width:90px;height:220px;background:rgba(212,32,42,.08)"></div>
      <h2 class="heading sports__title">Sports</h2>
      <p class="body-copy sports__lead">The 2021 Global Veterans Games will feature a total of 65 sports played in first class venues across the region. The 2021 sports include:</p>
      <div class="photo sports__photo" role="img" aria-label="Photo of a basketball on court"></div>
      <div class="slash slash--strong" style="left:250px;top:24px;width:90px;height:60px"></div>
      <div class="slash" style="left:225px;top:84px;width:100px;height:50px;background:rgba(212,32,42,.32)"></div>
      <ul class="sports__grid">
        <li class="sport"><svg><use href="#i-target"/></svg><span class="sport__name">Archery</span></li>
        <li class="sport"><svg><use href="#i-medal"/></svg><span class="sport__name">Athletics</span></li>
        <li class="sport"><svg><use href="#i-oval"/></svg><span class="sport__name">Badminton</span></li>
        <li class="sport"><svg><use href="#i-ball"/></svg><span class="sport__name">Baseball</span></li>
        <li class="sport"><svg><use href="#i-ball"/></svg><span class="sport__name">Basketball</span></li>
        <li class="sport"><svg><use href="#i-cup"/></svg><span class="sport__name">Canoe</span></li>
        <li class="sport"><svg><use href="#i-medal"/></svg><span class="sport__name">Cycling</span></li>
        <li class="sport"><svg><use href="#i-cup"/></svg><span class="sport__name">Dance Sports</span></li>
        <li class="sport"><svg><use href="#i-cup"/></svg><span class="sport__name">Dragonboat</span></li>
        <li class="sport"><svg><use href="#i-oval"/></svg><span class="sport__name">Football</span></li>
        <li class="sport"><svg><use href="#i-cup"/></svg><span class="sport__name">Flying Disc (Ultimate)</span></li>
        <li class="sport"><svg><use href="#i-cup"/></svg><span class="sport__name">Gateball</span></li>
        <li class="sport"><svg><use href="#i-flag"/></svg><span class="sport__name">Golf</span></li>
        <li class="sport"><svg><use href="#i-cup"/></svg><span class="sport__name">Handball</span></li>
        <li class="sport"><svg><use href="#i-medal"/></svg><span class="sport__name">Hockey</span></li>
        <li class="sport"><svg><use href="#i-medal"/></svg><span class="sport__name">Judo</span></li>
        <li class="sport"><svg><use href="#i-cup"/></svg><span class="sport__name">Karate</span></li>
        <li class="sport"><svg><use href="#i-cup"/></svg><span class="sport__name">Lifesaving</span></li>
        <li class="sport"><svg><use href="#i-cup"/></svg><span class="sport__name">Orienteering</span></li>
        <li class="sport"><svg><use href="#i-wave"/></svg><span class="sport__name">Rowing</span></li>
        <li class="sport"><svg><use href="#i-oval"/></svg><span class="sport__name">Rugby</span></li>
        <li class="sport"><svg><use href="#i-sail"/></svg><span class="sport__name">Sailing</span></li>
        <li class="sport"><svg><use href="#i-target"/></svg><span class="sport__name">Shooting</span></li>
        <li class="sport"><svg><use href="#i-ball"/></svg><span class="sport__name">Softball</span></li>
        <li class="sport"><svg><use href="#i-cup"/></svg><span class="sport__name">Soft Tennis</span></li>
        <li class="sport"><svg><use href="#i-medal"/></svg><span class="sport__name">Squash</span></li>
        <li class="sport"><svg><use href="#i-wave"/></svg><span class="sport__name">Swimming</span></li>
        <li class="sport"><svg><use href="#i-wave"/></svg><span class="sport__name">Water Polo</span></li>
        <li class="sport"><svg><use href="#i-medal"/></svg><span class="sport__name">Table Tennis</span></li>
        <li class="sport"><svg><use href="#i-medal"/></svg><span class="sport__name">Taekwondo</span></li>
        <li class="sport"><svg><use href="#i-ball"/></svg><span class="sport__name">Tennis</span></li>
        <li class="sport"><svg><use href="#i-cup"/></svg><span class="sport__name">Tenpin Bowling</span></li>
        <li class="sport"><svg><use href="#i-tri"/></svg><span class="sport__name">Triathlon</span></li>
        <li class="sport"><svg><use href="#i-cup"/></svg><span class="sport__name">Tug of War</span></li>
        <li class="sport"><svg><use href="#i-ball"/></svg><span class="sport__name">Volleyball</span></li>
        <li class="sport"><svg><use href="#i-bar"/></svg><span class="sport__name">Weightlifting</span></li>
      </ul>
    </article>
  </section>

  <section class="spread spread--travel" aria-label="Venues and tour packages pages">
    <article class="page">
      <div class="slash" style="left:150px;top:0;width:50px;height:130px"></div>
      <div class="slash" style="left:220px;top:0;width:40px;height:130px"></div>
      <div class="slash slash--grey" style="left:300px;top:0;width:40px;height:100px"></div>
      <h2 class="heading venues__title">Venues</h2>
      <div class="photo venues__map" role="img" aria-label="Colour-coded venue map of 59 disciplines of 35 sports across the Kansai prefectures"></div>
    </article>
    <article class="page">
      <div class="slash" style="left:180px;top:0;width:50px;height:120px"></div>
      <div class="slash" style="left:260px;top:0;width:40px;height:120px"></div>
      <h2 class="heading tour__title">Tour Packages</h2>
      <p class="body-copy tour__lead">Working with airline and local accommodation, travel and tour partners we have crafted tour packages with quality hotels conveniently located to the various sports venues as well as transport links. As no trip to Japan is complete without a visit to Tokyo we have included Japan's capital and some of the major sights in the package.</p>
      <p class="tour__sub">Package Include:</p>
      <ul class="tour__list tour__list--main">
        <li><svg width="16" height="16" viewBox="0 0 16 16"><path d="M1 9l14-5-3 6-4 1-2 4-1-4z"/></svg>Flights</li>
        <li><svg width="16" height="16" viewBox="0 0 16 16"><rect x="1" y="7" width="14" height="5"/><rect x="1" y="4" width="5" height="3"/><rect x="1" y="12" width="2" height="2"/><rect x="13" y="12" width="2" height="2"/></svg>Accommodation</li>
        <li><svg width="16" height="16" viewBox="0 0 16 16"><circle cx="8" cy="8" r="6" fill="none" stroke="#1d1d1f" stroke-width="2"/><circle cx="8" cy="8" r="2.5"/></svg>Breakfast Daily</li>
        <li><svg width="16" height="16" viewBox="0 0 16 16"><circle cx="5" cy="4" r="2"/><circle cx="11" cy="4" r="2"/><rect x="3" y="7" width="4" height="8"/><rect x="9" y="7" width="4" height="8"/></svg>Meet &amp; Greet, with<br>bilingual hosts</li>
      </ul>
      <ul class="tour__list tour__list--extra">
        <li><svg width="16" height="16" viewBox="0 0 16 16"><rect x="1" y="2" width="9" height="7" rx="1"/><rect x="6" y="7" width="9" height="7" rx="1" fill="#55565c"/></svg>Bilingual Local Guides</li>
        <li><svg width="16" height="16" viewBox="0 0 16 16"><rect x="1" y="6" width="14" height="5" rx="2"/><circle cx="4" cy="12" r="2"/><circle cx="12" cy="12" r="2"/></svg>Transport</li>
        <li><svg width="16" height="16" viewBox="0 0 16 16"><path d="M1 11h11l3-4H5z"/><rect x="1" y="12" width="14" height="1.5"/></svg>Bullet Train</li>
        <li><svg width="16" height="16" viewBox="0 0 16 16"><rect x="1" y="5" width="14" height="9" rx="1"/><rect x="5" y="3" width="6" height="2"/><circle cx="8" cy="9.5" r="2.5" fill="#fff"/></svg>Sightseeing</li>
      </ul>
      <div class="slash slash--line" style="left:405px;top:268px;width:6px;height:22px"></div>
      <div class="slash slash--line" style="left:418px;top:268px;width:12px;height:22px"></div>
      <div class="slash slash--grey" style="left:160px;top:280px;width:30px;height:120px"></div>
      <div class="photo tour__photo" role="img" aria-label="Photo of stacked luggage on airport trolleys"></div>
      <div class="slash" style="left:290px;top:340px;width:40px;height:80px;background:rgba(212,32,42,.3)"></div>
      <div class="slash slash--strong" style="left:370px;top:330px;width:80px;height:110px"></div>
    </article>
  </section>

</main>
</body>
</html>
```